House Builder and Property Development Card Design and Logo

I need a business card design for a building and property development company.
Colour scheme of Dark Grey and Green, I would like it bold, sharp and professional.
No logo yet done, I'm open to options but please stay away from the usual- house, roof, hammers etc.
Thanks Rob

Please be aware that on the business card information section the WHRC # 5528391 is a licence number and my phone number 0492837165. The numbers are close together and could be mistaken as one whole number 

Thank you

                                   

Industry/Entity Type

Building

Contact Information for Business Card

VARGA BUILD & DEVELOPMENT.
Residential Building & Property Development
Robert Varga - Director
WHRC # 5528391
0492837165
rob@vargabuild.example.com.au

Requirements
Must have
• Bold Business name
Dark grey and green colours
Should not have
• roof outline or hammer logo

```html
<!DOCTYPE html>
<html lang="en">
<head>
<meta charset="utf-8">
<title>Varga Build &amp; Development – Business Card</title>
<link rel="stylesheet" href="https://fonts.googleapis.com/css2?family=Lato:wght@300;400;700;900&family=Oswald:wght@500&display=swap">
<style>
  :root {
    --canvas: #d9d9d7;
    --card: #1d1d1e;
    --green: #13994a;
    --white: #f4f4f4;
    --shadow: rgba(0, 0, 0, 0.28);
  }
  * { margin: 0; padding: 0; box-sizing: border-box; }
  html, body {
    width: 1200px;
    height: 926px;
    overflow: hidden;
    background: var(--canvas);
    font-family: "Lato", sans-serif;
  }
  .sheet {
    position: relative;
    width: 1200px;
    height: 926px;
  }
  .card {
    position: absolute;
    left: 250px;
    width: 700px;
    height: 400px;
    background: var(--card);
    box-shadow: 0 10px 28px var(--shadow);
    overflow: hidden;
  }
  .card--front { top: 43px; }
  .card--back { top: 483px; }

  /* Front */
  .brand-mark {
    position: absolute;
    left: 188px;
    top: 42px;
    width: 88px;
    height: 88px;
    border-radius: 50%;
    background: var(--green);
    border: 5px solid var(--white);
  }
  .brand-mark-name {
    position: absolute;
    left: 150px;
    top: 138px;
    width: 164px;
    text-align: center;
    font-weight: 700;
    font-size: 13px;
    letter-spacing: 3px;
    color: var(--green);
  }
  .holder {
    position: absolute;
    right: 454px;
    top: 178px;
    text-align: right;
  }
  .holder-name {
    font-family: "Oswald", sans-serif;
    font-weight: 500;
    font-size: 29px;
    letter-spacing: -0.3px;
    color: var(--white);
    text-transform: uppercase;
    line-height: 1;
  }
  .holder-role {
    margin-top: 8px;
    font-size: 14px;
    letter-spacing: 1px;
    color: var(--green);
    text-transform: uppercase;
  }
  .divider {
    position: absolute;
    left: 326px;
    width: 2px;
    background: var(--white);
  }
  .divider--upper { top: 18px; height: 150px; }
  .divider--lower { top: 282px; height: 56px; }
  .company {
    position: absolute;
    left: 346px;
    top: 84px;
    width: 330px;
  }
  .company-name {
    font-weight: 900;
    font-size: 20px;
    color: var(--green);
    text-transform: uppercase;
    letter-spacing: 0;
    white-space: nowrap;
    line-height: 1.2;
  }
  .company-tagline {
    margin-top: 5px;
    font-size: 13px;
    color: var(--white);
    letter-spacing: 0.9px;
    white-space: nowrap;
  }
  .contact {
    position: absolute;
    left: 346px;
    top: 196px;
    list-style: none;
    font-size: 15px;
    line-height: 22px;
    color: var(--white);
    letter-spacing: 0.6px;
  }
  .contact-label {
    color: var(--green);
    font-weight: 700;
  }
  .accent-band {
    position: absolute;
    left: 0;
    bottom: 0;
    width: 100%;
    height: 46px;
    background: var(--green);
  }

  /* Back */
  .back-mark {
    position: absolute;
    left: 306px;
    top: 116px;
    width: 88px;
    height: 88px;
    border-radius: 50%;
    background: var(--green);
    border: 5px solid var(--white);
  }
  .back-name {
    position: absolute;
    top: 238px;
    width: 100%;
    text-align: center;
    font-weight: 400;
    font-size: 15px;
    letter-spacing: 2.6px;
    color: var(--green);
  }
</style>
</head>
<body>
<main class="sheet">
  <section class="card card--front" aria-label="Business card front">
    <div class="brand-mark"></div>
    <div class="brand-mark-name">VARGA</div>
    <div class="holder">
      <p class="holder-name">Robert Varga</p>
      <p class="holder-role">Director</p>
    </div>
    <span class="divider divider--upper"></span>
    <span class="divider divider--lower"></span>
    <div class="company">
      <h1 class="company-name">Varga Build &amp; Development</h1>
      <p class="company-tagline">Residential Building &amp; Property Development</p>
    </div>
    <ul class="contact">
      <li><span class="contact-label">licence:</span> WHRC # 5528391</li>
      <li><span class="contact-label">phone:</span> 0492837165</li>
      <li><span class="contact-label">email:</span> rob@vargabuild.example.com.au</li>
    </ul>
    <div class="accent-band"></div>
  </section>

  <section class="card card--back" aria-label="Business card back">
    <div class="back-mark"></div>
    <p class="back-name">CALDER CONSULTING GROUP LLC</p>
  </section>
</main>
</body>
</html>
```